bottle label/ product label for smoothies (ultra fresh)

Please create a bottle label for our smoothies for retail distribution.
It's important that the following key features are clearly stated:

Ultra-fresh

Handmade

No preservatives

Not heat-treated

No added sugar

The base of the product label should be transparent, so that the color and content of the smoothie can be seen clearly.

We are a young, dynamic company. Our values are honesty, ultra-freshness, and authenticity — and we are the only ones producing this type of product in our country. We are positioned in the premium segment.

Design style: Modern, clean, and natural — but not playful or childish.

Example product: Kelu Kelu (Mango, Pineapple, Lemon, Passion Fruit, Orange)

Wenn du möchtest, kann ich auch gleich einen konkreten Vorschlag für das Etikettendesign auf Englisch oder einen Entwurfstext für das Label selbst erstellen. Sag einfach Bescheid!

Target Market(s)

trade - convenience

Industry/Entity Type

trade

Font styles to use
Sans Serif

Requirements
Must have
• sales- features: Ultra-fresh Handmade No preservatives Not heat-treated No added sugar

```html
<!DOCTYPE html>
<html lang="en">
<head>
<meta charset="utf-8">
<title>SOLVA – Kelu Kelu smoothie label</title>
<link href="https://fonts.googleapis.com/css2?family=Allura&family=Archivo:wght@500;600;700&display=swap" rel="stylesheet">
<style>
  :root {
    --band-yellow: #fed95a;
    --disc-yellow: #fdd95a;
    --pattern-cream: #fdf3d6;
    --ink: #1c1c1c;
    --paper: #ffffff;
  }
  * { margin: 0; padding: 0; box-sizing: border-box; }
  html, body {
    width: 1200px;
    height: 1200px;
    overflow: hidden;
    background: var(--paper);
  }
  .label {
    position: absolute;
    left: 251px;
    top: 273px;
    width: 697px;
    height: 653px;
  }
  .fruit-pattern {
    position: absolute;
    left: 56px;
    top: 42px;
    width: 588px;
    height: 574px;
    background: radial-gradient(ellipse at 50% 50%, #fef8e6 0%, var(--pattern-cream) 100%);
  }
  .band {
    position: absolute;
    left: 0;
    width: 697px;
    background: var(--band-yellow);
  }
  .band--top { top: 0; height: 44px; clip-path: polygon(0 0, 100% 0, 100% 100%, 55% 94%, 0 82%); }
  .band--bottom { top: 612px; height: 41px; clip-path: polygon(0 8%, 30% 0, 70% 6%, 100% 10%, 100% 100%, 0 100%); }

  .brand-name {
    position: absolute;
    left: 155px;
    top: 330px;
    transform: translate(-50%, -50%) rotate(-90deg);
    font-family: "Archivo", sans-serif;
    font-weight: 700;
    font-size: 118px;
    letter-spacing: 0.02em;
    line-height: 1;
    color: var(--ink);
    white-space: nowrap;
  }
  .flavour-disc {
    position: absolute;
    left: 274px;
    top: 102px;
    width: 200px;
    height: 200px;
    border-radius: 50%;
    background: var(--disc-yellow);
  }
  .flavour-name {
    position: absolute;
    left: 374px;
    top: 202px;
    transform: translate(-50%, -50%);
    font-family: "Allura", cursive;
    font-size: 96px;
    line-height: 1;
    color: var(--ink);
    white-space: nowrap;
  }
  .ingredients {
    position: absolute;
    left: 376px;
    top: 322px;
    transform: translateX(-50%);
    font-family: "Archivo", sans-serif;
    font-weight: 600;
    font-size: 17.5px;
    line-height: 21px;
    color: var(--ink);
    text-align: center;
    white-space: nowrap;
  }
  .claim {
    position: absolute;
    left: 370px;
    transform: translateX(-50%);
    font-family: "Archivo", sans-serif;
    color: var(--ink);
    white-space: nowrap;
  }
  .claim--fresh { top: 417px; font-size: 14px; font-weight: 600; }
  .claim--handmade { top: 442px; font-size: 13px; font-weight: 700; letter-spacing: 0.88em; margin-left: 0.44em; }

  .badges {
    position: absolute;
    left: 240px;
    top: 479px;
    width: 260px;
    height: 90px;
  }
  .badge-ring { fill: none; stroke: var(--ink); stroke-width: 2.2; }
  .badge-glyph { fill: none; stroke: var(--ink); stroke-width: 1.8; }
  .badge-glyph--solid { fill: var(--ink); }
  .badge-text {
    font-family: "Archivo", sans-serif;
    font-weight: 600;
    font-size: 10.5px;
    fill: var(--ink);
  }
</style>
</head>
<body>
  <main class="label">
    <div class="fruit-pattern" role="img" aria-label="Faint line drawings of mangoes, lemons and passion fruit scattered across the label"></div>
    <div class="band band--top"></div>
    <div class="band band--bottom"></div>

    <div class="brand-name">SOLVA</div>

    <div class="flavour-disc"></div>
    <div class="flavour-name">kelu kelu</div>

    <p class="ingredients">MANGO, PINEAPPLE, LEMON,<br>PASSION FRUIT, ORANGE</p>

    <p class="claim claim--fresh">ULTRA-FRESH</p>
    <p class="claim claim--handmade">HANDMADE</p>

    <svg class="badges" viewBox="0 0 260 90" aria-label="Product claims">
      <defs>
        <path id="arc-1" d="M13.1 56.6 A34 34 0 1 1 76.9 56.6"/>
        <path id="arc-2" d="M97.1 56.6 A34 34 0 1 1 160.9 56.6"/>
        <path id="arc-3" d="M182.1 56.6 A34 34 0 1 1 245.9 56.6"/>
      </defs>

      <g class="badge badge--heat">
        <text class="badge-text"><textPath href="#arc-1" startOffset="50%" text-anchor="middle">NOT HEAT-TREATED</textPath></text>
        <circle class="badge-ring" cx="45" cy="45" r="23"/>
        <line class="badge-glyph" x1="45" y1="33" x2="45" y2="52"/>
        <circle class="badge-glyph badge-glyph--solid" cx="45" cy="55" r="3.6"/>
        <line class="badge-ring" x1="29" y1="29" x2="61" y2="61"/>
      </g>

      <g class="badge badge--preservatives">
        <text class="badge-text"><textPath href="#arc-2" startOffset="50%" text-anchor="middle">NO PRESERVATIVES</textPath></text>
        <circle class="badge-ring" cx="129" cy="45" r="23"/>
        <rect class="badge-glyph" x="125" y="31" width="8" height="26" rx="4"/>
        <rect class="badge-glyph badge-glyph--solid" x="126" y="44" width="6" height="12" rx="3"/>
        <line class="badge-ring" x1="113" y1="29" x2="145" y2="61"/>
      </g>

      <g class="badge badge--sugar">
        <text class="badge-text"><textPath href="#arc-3" startOffset="50%" text-anchor="middle">NO ADDED SUGAR</textPath></text>
        <circle class="badge-ring" cx="214" cy="45" r="23"/>
        <rect class="badge-glyph" x="202" y="35" width="12" height="12" rx="2"/>
        <rect class="badge-glyph" x="211" y="43" width="12" height="12" rx="2"/>
        <line class="badge-ring" x1="198" y1="29" x2="230" y2="61"/>
      </g>
    </svg>
  </main>
</body>
</html>
```